The Perfect Business Card for PineHarbor

I am looking for a business card which beautifully incorporates my logo, reflects my business and looks special, elegant and clean.

```html
<!DOCTYPE html>
<html lang="en">
<head>
<meta charset="utf-8">
<title>PineHarbor Business Card</title>
<link href="https://fonts.googleapis.com/css2?family=Montserrat:wght@400;700&display=swap" rel="stylesheet">
<style>
  :root {
    --card-green: #7a9c40;
    --ring-green: #5c7d31;
    --paper: #ffffff;
    --backdrop: #d9d9d9;
    --ink-light: #ffffff;
  }
  html, body {
    margin: 0;
    padding: 0;
    width: 1200px;
    height: 1164px;
    overflow: hidden;
    background: var(--backdrop);
    font-family: "Montserrat", sans-serif;
  }
  .canvas {
    position: relative;
    width: 1200px;
    height: 1164px;
  }
  .card {
    position: absolute;
    left: 150px;
    width: 900px;
    height: 513px;
    border-radius: 22px;
    background: var(--card-green);
    overflow: hidden;
    box-shadow: 0 4px 10px rgba(0,0,0,0.18);
    color: var(--ink-light);
  }
  .card--front { top: 46px; }
  .card--back { top: 605px; }

  .card__ring {
    position: absolute;
    inset: 0;
    width: 900px;
    height: 513px;
  }

  .brand {
    position: absolute;
    display: flex;
    align-items: center;
    gap: 14px;
  }
  .brand__mark {
    border: 2px solid var(--ink-light);
    border-radius: 50%;
    box-sizing: border-box;
  }
  .brand__name {
    font-weight: 400;
    color: var(--ink-light);
    letter-spacing: 0.5px;
  }

  .card--front .brand { left: 74px; top: 62px; }
  .card--front .brand__mark { width: 100px; height: 100px; }
  .card--front .brand__name { font-size: 34px; }

  .card--back .brand {
    left: 50%;
    top: 50%;
    transform: translate(-50%, -50%);
    gap: 20px;
  }
  .card--back .brand__mark { width: 150px; height: 150px; }
  .card--back .brand__name { font-size: 52px; }

  .contact {
    position: absolute;
    left: 74px;
    top: 232px;
  }
  .contact__name {
    margin: 0;
    font-size: 25px;
    font-weight: 700;
    letter-spacing: 0.5px;
    text-transform: uppercase;
  }
  .contact__title {
    margin: 2px 0 0;
    font-size: 19px;
    font-weight: 400;
  }
  .contact__address {
    margin: 32px 0 0;
    font-size: 19px;
    line-height: 26px;
    font-style: normal;
  }
  .contact__list {
    list-style: none;
    margin: 18px 0 0;
    padding: 0;
    font-size: 19px;
    line-height: 26px;
  }
  .contact__item {
    display: flex;
    align-items: center;
    gap: 12px;
  }
  .contact__icon {
    width: 15px;
    height: 15px;
    flex: none;
  }
</style>
</head>
<body>
<main class="canvas">

  <section class="card card--front" aria-label="Business card front">
    <svg class="card__ring" viewBox="0 0 900 513" aria-hidden="true">
      <circle cx="668" cy="262" r="258" fill="var(--paper)" stroke="var(--ring-green)" stroke-width="6"/>
    </svg>

    <div class="brand">
      <span class="brand__mark"></span>
      <span class="brand__name">PineHarbor</span>
    </div>

    <div class="contact">
      <h1 class="contact__name">Dr. Maren Holtwick</h1>
      <p class="contact__title">Dipl. Naturheilpraktikerin (TEN)</p>
      <address class="contact__address">Lindenweg 7<br>8032 Seeberg</address>
      <ul class="contact__list">
        <li class="contact__item">
          <svg class="contact__icon" viewBox="0 0 16 16" aria-hidden="true"><path d="M3 1.5l3 .5 1 3.5-2 1.2c.9 2 2.4 3.5 4.3 4.3l1.2-2 3.5 1 .5 3c-.3 1-1.2 1.5-2.2 1.5C6.6 14.5 1.5 9.4 1.5 3.7 1.5 2.7 2 1.8 3 1.5z" fill="currentColor"/></svg>
          +41 (0) 70 555 01 23
        </li>
        <li class="contact__item">
          <svg class="contact__icon" viewBox="0 0 16 16" aria-hidden="true"><rect x="1" y="3" width="14" height="10" fill="currentColor"/><path d="M1.5 3.5L8 9l6.5-5.5" fill="none" stroke="var(--card-green)" stroke-width="1.4"/></svg>
          info@pineharbor.ch
        </li>
        <li class="contact__item">
          <svg class="contact__icon" viewBox="0 0 16 16" aria-hidden="true"><g fill="none" stroke="currentColor" stroke-width="1.3"><circle cx="8" cy="8" r="6.5"/><ellipse cx="8" cy="8" rx="3" ry="6.5"/><path d="M1.5 8h13M2.5 4.8h11M2.5 11.2h11"/></g></svg>
          www.pineharbor.ch
        </li>
      </ul>
    </div>
  </section>

  <section class="card card--back" aria-label="Business card back">
    <div class="brand">
      <span class="brand__mark"></span>
      <span class="brand__name">PineHarbor</span>
    </div>
  </section>

</main>
</body>
</html>
```